Letterhead and email signiture

Hello,

I have an example of a letterhead that we need. The one we have constandly moves if we paste any information in it. We are looking for one that is permanent. We only need the top of the letterhead on the first page but the bottom on each and every page afterward.

It does not have to be exactly what I am providing here. Please take a look at the website and maybe you will have a better idea.

We are looking to do something similar for an email signature

Marvistoinc.com

```html
<!DOCTYPE html>
<html lang="en">
<head>
<meta charset="utf-8">
<title>Marvisto Inc – Letterhead and Business Card</title>
<link href="https://fonts.googleapis.com/css2?family=Open+Sans:wght@700&family=Roboto:wght@400;700&family=Arimo:wght@400&family=Cabin+Condensed:wght@400&display=swap" rel="stylesheet">
<style>
  :root {
    --backdrop: #bcbcbc;
    --paper: #ffffff;
    --ink-black: #161616;
    --brand-green: #a4bf38;
    --brand-blue: #3d87d6;
    --text-grey: #4a4a4a;
    --rule-grey: #8a8a8a;
  }
  * { margin: 0; padding: 0; box-sizing: border-box; }
  html, body { width: 884px; height: 1200px; overflow: hidden; }
  body {
    background: var(--backdrop);
    position: relative;
    font-family: "Arimo", Arial, sans-serif;
    color: var(--text-grey);
  }
  .sheet {
    position: absolute;
    background: var(--paper);
    box-shadow: 2px 3px 5px rgba(0,0,0,0.35);
    overflow: hidden;
  }
  .letterhead { left: 160px; top: 41px; width: 565px; height: 800px; }
  .business-card { left: 139px; top: 879px; width: 607px; height: 242px; }

  .header-wave { position: absolute; left: 0; top: 0; width: 100%; display: block; }
  .brand-name {
    position: absolute;
    font-family: "Open Sans", Arial, sans-serif;
    font-weight: 700;
    color: #ffffff;
    letter-spacing: -0.5px;
    line-height: 1;
    white-space: nowrap;
  }
  .letterhead .brand-name { left: 38px; top: 28px; font-size: 23px; }
  .business-card .brand-name { left: 32px; top: 34px; font-size: 28px; }

  .salutation { position: absolute; left: 51px; top: 247px; font-size: 12px; }
  .letter-text { position: absolute; left: 51px; top: 283px; width: 466px; }
  .letter-text p { font-size: 8.9px; line-height: 11.7px; margin-bottom: 10px; }
  .closing { position: absolute; left: 51px; top: 524px; font-size: 7px; }
  .signature {
    position: absolute; left: 42px; top: 550px;
    font-family: "Cabin Condensed", "Arial Narrow", sans-serif;
    font-size: 15px; letter-spacing: -0.6px; color: #333;
  }

  .contact-row { display: flex; align-items: center; white-space: nowrap; }
  .contact-row svg { fill: var(--brand-blue); flex: none; }
  .letter-footer { position: absolute; left: 84px; top: 750px; width: 397px; text-align: center; }
  .letter-footer .contact-row { justify-content: center; font-size: 8.6px; gap: 3px; }
  .letter-footer .contact-row .gap { width: 5px; }
  .letter-footer .rule { height: 1px; background: var(--rule-grey); margin: 3px 0 4px; }
  .letter-footer .notice { font-size: 8.6px; }

  .card-person { position: absolute; right: 24px; top: 100px; text-align: right; }
  .person-name { font-family: "Roboto", Arial, sans-serif; font-size: 21px; font-weight: 700; color: var(--brand-blue); line-height: 1; letter-spacing: 0.2px; }
  .person-role { font-size: 15.5px; line-height: 1; margin-top: 5px; color: var(--text-grey); }
  .card-notice { position: absolute; left: 34px; top: 155px; font-size: 15px; line-height: 19px; }
  .card-rule { position: absolute; left: 34px; top: 196px; width: 456px; height: 1px; background: #555; }
  .card-contacts { position: absolute; left: 34px; top: 204px; font-size: 15.5px; gap: 5px; }
  .card-contacts .gap { width: 9px; }
</style>
</head>
<body>

<section class="sheet letterhead">
  <svg class="header-wave" viewBox="0 0 959 170" aria-hidden="true">
    <path fill="var(--brand-green)" d="M0,0 V80 C60,135 150,162 250,162 C420,162 570,122 680,90 L720,60 L959,40 V0 Z"/>
    <path fill="var(--brand-blue)" d="M0,0 H959 V140 C915,95 860,80 785,84 C620,95 480,135 330,142 L200,100 L0,40 Z"/>
    <path fill="var(--ink-black)" d="M0,0 H959 V122 C920,80 860,60 780,68 C600,90 420,141 240,141 C140,141 60,110 0,62 Z"/>
  </svg>
  <div class="brand-name">MARVISTO INC</div>

  <p class="salutation">Dear Mr. Harper,</p>
  <div class="letter-text">
    <p>Lorem ipsum dolor sit amet, consectetuer adipiscing elit, sed diam nonmmy nibh euismod tincidunt ut laor eet dolore magna aliquam erat volutpat. Ut wisi enim ad minim veniam, quis nostrud exerci tationmcorper suscipit lobortis nisl ut aliquip ex ea commodo consequat. Duis autem vel eum iriure dolor in hendrerit in vulputate velit esse molestie consequat, vel illum dolore eu feugiat</p>
    <p>Rorem ipsum dolor sit amet, consectetuer adipiscing elit, sed diam nonmmy nibh euismod tincidunt ut laor eet dolore magna aliquam erat volutpat. Ut wisi enim ad minim veniam, quis nostrud exerci tationmcorper suscipit lobortis nisl ut aliquip ex ea commodo consequat. Duis autem vel eum iriure dolor in hendrerit in vulputate velit esse molest</p>
    <p>Dorem ipsum dolor sit amet, consectetuer adipiscing elit, sed diam nonmmy nibh euismod tincidunt ut laor eet dolore magna aliquam erat volutpat. Ut wisi enim ad minim veniam, quis nostrud exerci tationmcorper suscipit lobortis nisl ut aliquip ex ea commodo consequat. Duis autem vel eum iriure dolor in hendrerit in suscipit lobortis nisl ut aliquip ex ea commodo consequat. Duis autem vel eum iriure dolor in hendrerit in vulputate velit esse molestie consequat, vel illum</p>
    <p>Sorem ipsum dolor sit amet, consectetuer adipiscing elit, sed diam nonmmy nibh euismod tincidunt ut laor eet dolore magna aliquam erat volutpat. Ut wisi enim ad minim veniam, quis nostrud exerci tationmcorper suscipit lobortis nisl ut aliquip ex ea commodo consequat. Duis autem vel eum iriure dolor in</p>
  </div>
  <p class="closing">Sincerely,</p>
  <p class="signature">Rowan Jelby</p>

  <footer class="letter-footer">
    <div class="contact-row">
      <svg width="8" height="7" viewBox="0 0 16 14"><path d="M1,5 C1,2 4,1 8,1 C12,1 15,2 15,5 L12,5 L11,3 H5 L4,5 Z M3,6 H13 L15,13 H1 Z"/></svg>
      <span>305-555-0142</span><span class="gap"></span>
      <svg width="8" height="7" viewBox="0 0 16 14"><path d="M1,5 C1,2 4,1 8,1 C12,1 15,2 15,5 L12,5 L11,3 H5 L4,5 Z M3,6 H13 L15,13 H1 Z"/></svg>
      <span class="gap"></span><span>904-555-0187</span><span class="gap"></span>
      <svg width="8" height="8" viewBox="0 0 16 16"><circle cx="8" cy="8" r="7.5"/><path fill="#fff" d="M5,3 C7,4 6,6 8,7 C9,9 6,10 6,13 C4,11 3,9 4,7 Z M11,9 C12,10 12,12 11,13 C10,12 10,10 11,9 Z"/></svg>
      <span class="gap"></span><span>MARVISTOINC.COM</span>
    </div>
    <div class="rule"></div>
    <p class="notice">This document is confidential and intended solely for investigative purposes by Marvisto Inc.</p>
  </footer>
</section>

<section class="sheet business-card">
  <svg class="header-wave" viewBox="0 0 959 200" aria-hidden="true">
    <rect x="0" y="0" width="959" height="40" fill="var(--ink-black)"/>
    <g transform="translate(0,32)">
      <path fill="var(--brand-green)" d="M0,0 V80 C60,135 150,162 250,162 C420,162 570,122 680,90 L720,60 L959,40 V0 Z"/>
      <path fill="var(--brand-blue)" d="M0,0 H959 V140 C915,95 860,80 785,84 C620,95 480,135 330,142 L200,100 L0,40 Z"/>
      <path fill="var(--ink-black)" d="M0,0 H959 V122 C920,80 860,60 780,68 C600,90 420,141 240,141 C140,141 60,110 0,62 Z"/>
    </g>
  </svg>
  <div class="brand-name">MARVISTO INC</div>

  <div class="card-person">
    <p class="person-name">DANIEL HARPER</p>
    <p class="person-role">Manager</p>
  </div>
  <p class="card-notice">This document is confidential and intended<br>solely for investigative purposes by Marvisto Inc.</p>
  <div class="card-rule"></div>
  <div class="contact-row card-contacts">
    <svg width="13" height="11" viewBox="0 0 16 14"><path d="M1,5 C1,2 4,1 8,1 C12,1 15,2 15,5 L12,5 L11,3 H5 L4,5 Z M3,6 H13 L15,13 H1 Z"/></svg>
    <span>305-555-0142</span><span class="gap"></span>
    <svg width="13" height="11" viewBox="0 0 16 14"><path d="M1,5 C1,2 4,1 8,1 C12,1 15,2 15,5 L12,5 L11,3 H5 L4,5 Z M3,6 H13 L15,13 H1 Z"/></svg>
    <span class="gap"></span><span>904-555-0187</span><span class="gap"></span>
    <svg width="13" height="13" viewBox="0 0 16 16"><circle cx="8" cy="8" r="7.5"/><path fill="#fff" d="M5,3 C7,4 6,6 8,7 C9,9 6,10 6,13 C4,11 3,9 4,7 Z M11,9 C12,10 12,12 11,13 C10,12 10,10 11,9 Z"/></svg>
    <span class="gap"></span><span>MARVISTOINC.COM</span>
  </div>
</section>

</body>
</html>
```